Simple, elegant, business card design required

Hi designers,I am looking for a simple yet elegant business card design.

Please make use of my logo (attached); you are free to tweak the logo should you wish to do so.

Our business is involved in many different fields - almost all of them involved in some form of "design", so that's really one of the key things I want to portray. I do not wish to specify which field of design, exactly.

I prefer white on black (or just monochromatic), but if you have a different, creative idea, I am open to that too.

You can use artsy photographs provided that you have the license to use those. Please feel free to ask me any questions.
Updates

Project Deadline Extended Reason: Small extension for potential revisions. Did not get the time to provide as much feedback as I can. Added Wednesday, July 09, 2014

Target Market(s)

High-end customers looking for design consultancy

Industry/Entity Type

Business

Contact Information for Business Card

Name: Gareth Moonfield
Position: Creative Director
Mobile: +155603928174
Address: Barrow Lane, Holbrook upon Teme, Ashvaleshire GL12 4RT
Website: torvakest.com (not launched yet)

Requirements
Must have
• Design layout must be clean, original, and text must be readable when printed.
Should not have
• ~ No business card templates please. Anyone using this will be reported.
• ~ Please don't spam entries.

```html
<!DOCTYPE html>
<html lang="en">
<head>
<meta charset="UTF-8">
<title>Gareth Moonfield – Business Card</title>
<link rel="stylesheet" href="https://fonts.googleapis.com/css2?family=Roboto+Condensed:wght@300;400;700&display=swap">
<style>
  :root {
    --ink: #0d0d0d;
    --ink-soft: #1c1a1a;
    --glow: #3c3b3b;
    --paper: #ffffff;
    --rule: #2a2a2a;
  }
  * { margin: 0; padding: 0; box-sizing: border-box; }
  html, body {
    width: 1200px;
    height: 702px;
    overflow: hidden;
    background: var(--ink);
  }
  .card {
    position: relative;
    width: 1200px;
    height: 702px;
    overflow: hidden;
    font-family: "Roboto Condensed", "Arial Narrow", sans-serif;
    background: radial-gradient(ellipse 55% 60% at 50% 38%, var(--glow) 0%, #1f1f1f 55%, var(--ink) 100%);
  }
  .top-band {
    position: absolute; left: 0; top: 0; width: 100%; height: 53px;
    background: linear-gradient(var(--ink), #222);
  }
  .brand-band {
    position: absolute; left: 0; top: 57px; width: 100%; height: 126px;
    background: var(--paper);
    border-bottom: 5px solid var(--rule);
  }
  .brand-mark {
    position: absolute; left: 418px; top: 13px; width: 176px; height: 101px;
    background: var(--ink-soft);
  }
  .brand-name {
    position: absolute; left: 611px; top: 47px;
    font-size: 30px; font-weight: 400; letter-spacing: 5px;
    color: var(--ink-soft); line-height: 1;
  }
  .identity {
    position: absolute; left: 0; top: 302px; width: 100%;
    text-align: center; color: var(--paper);
  }
  .identity .name {
    font-size: 45px; font-weight: 700; line-height: 1; letter-spacing: 0.2px;
  }
  .identity .role {
    font-size: 38px; font-weight: 300; line-height: 1; margin-top: 6px;
  }
  .contact-band {
    position: absolute; left: 0; top: 531px; width: 100%; height: 52px;
    background: var(--paper);
  }
  .contact-item {
    position: absolute; top: 2px; display: flex; align-items: center;
    font-size: 46px; font-weight: 400; color: var(--ink); line-height: 48px;
    letter-spacing: 1.5px;
  }
  .contact-item svg { display: block; margin-right: 10px; }
  .contact-item.phone { left: 157px; }
  .contact-item.web { left: 569px; }
  .address-band {
    position: absolute; left: 0; top: 589px; width: 100%; height: 53px;
    background: var(--ink);
    border-top: 1px solid #888;
    border-bottom: 3px solid var(--paper);
    color: var(--paper);
    text-align: center;
    font-size: 34px; font-weight: 400; line-height: 50px;
  }
</style>
</head>
<body>
  <div class="card">
    <div class="top-band"></div>

    <header class="brand-band">
      <div class="brand-mark" aria-hidden="true"></div>
      <div class="brand-name">TORVAKEST</div>
    </header>

    <section class="identity">
      <h1 class="name">GARETH MOONFIELD</h1>
      <p class="role">Creative Director</p>
    </section>

    <section class="contact-band">
      <div class="contact-item phone">
        <svg width="44" height="44" viewBox="0 0 44 44" aria-hidden="true">
          <rect x="1" y="1" width="42" height="42" rx="6" fill="#0d0d0d"/>
          <path d="M15 9c-2 1-4 3-4 6 0 8 10 20 18 20 3 0 5-2 6-4l-5-5-3 2c-3-1-7-6-8-9l2-3z" fill="#fff"/>
        </svg>
        <span>+155603928174</span>
      </div>
      <div class="contact-item web">
        <svg width="40" height="40" viewBox="0 0 40 40" aria-hidden="true" fill="none" stroke="#0d0d0d" stroke-width="2.5">
          <circle cx="20" cy="20" r="17"/>
          <ellipse cx="20" cy="20" rx="7.5" ry="17"/>
          <line x1="20" y1="3" x2="20" y2="37"/>
          <line x1="3" y1="20" x2="37" y2="20"/>
          <path d="M6 11h28M6 29h28"/>
        </svg>
        <span>www.torvakest.com</span>
      </div>
    </section>

    <footer class="address-band">Barrow Lane, Holbrook upon Teme, Ashvaleshire GL12 4RT</footer>
  </div>
</body>
</html>
```